Brochure Annual Report Design

I want to create a brochure / annual report for our company. Can you help me. I like this design. https://plumvaultdesigns.net/Zorvik/4829175-Annual-Report-2018. Here is our company website www.brimdental.com. Please take the logo from there. Our website needs an upgrade in how it looks. I would like the brochure annual report and the website to look somewhat congruent. I also want to create a very high end magazine that is fun for our company eventually.

We are a company that helps dentists create better practices by really improving the way they do business and motivating their teams. As a result they have more fun, more profit, happier team members, and they all have better lives.

Target Market(s)

dentist

Industry/Entity Type

Dental

Number of Pages Required

5+ page

Colors
0255a3
85cae6
ffffff

Requirements
Must have
• Must look really good.
Nice to have
• Any creative suggestions are welcomed. I need a website that looks congruent to the brochure and annual report. I also want to create a very high end magazine that is fun for our company eventually.
Should not have
• I don't like low quality design.

```html
<!DOCTYPE html>
<html lang="en">
<head>
<meta charset="utf-8">
<title>Brim Dental — Annual Report 2018 Cover Spread</title>
<link rel="stylesheet" href="https://fonts.googleapis.com/css2?family=Montserrat:wght@300;600;800&family=Open+Sans:wght@400;600&display=swap">
<style>
  :root {
    --brand-blue: #0255a3;
    --sky-blue: #85cae6;
    --mid-blue: #5fa3c4;
    --white: #ffffff;
    --page-back: #f5f5f6;
    --page-front: #e4e6e9;
    --canvas: #eceef1;
    --ink: #1d1d1f;
    --photo-dark: #3a2d27;
    --photo-light: #c9cdd2;
  }
  * { margin: 0; padding: 0; box-sizing: border-box; }
  html, body { width: 1200px; height: 900px; overflow: hidden; background: var(--canvas); }
  .spread {
    position: absolute; left: 150px; top: 132px;
    width: 900px; height: 636px;
    box-shadow: 0 12px 30px rgba(0,0,0,0.12);
    font-family: "Open Sans", sans-serif;
  }
  .spread-art { position: absolute; inset: 0; display: block; }
  .brand-name {
    font-family: "Montserrat", sans-serif;
    font-weight: 600; color: var(--brand-blue);
    display: flex; align-items: center; gap: 8px;
    letter-spacing: 0.01em;
  }
  .brand-mark { width: 12px; height: 12px; border-radius: 50%; background: var(--brand-blue); }
  .back-cover .brand-name { position: absolute; left: 58px; top: 160px; font-size: 24px; }
  .contact-list { position: absolute; left: 58px; top: 206px; list-style: none; font-size: 10.5px; color: var(--ink); }
  .contact-list li { display: flex; align-items: center; gap: 10px; margin-bottom: 10px; line-height: 1.3; }
  .contact-icon { width: 16px; height: 16px; flex: none; }
  .front-cover .brand-name { position: absolute; right: 120px; top: 52px; font-size: 26px; }
  .report-title { position: absolute; right: 40px; top: 300px; text-align: right; }
  .report-kicker {
    font-family: "Montserrat", sans-serif; font-weight: 300;
    font-size: 26px; letter-spacing: 0.04em; color: var(--mid-blue); line-height: 1;
  }
  .report-heading {
    font-family: "Montserrat", sans-serif; font-weight: 800;
    font-size: 30px; color: var(--brand-blue); line-height: 1.1;
  }
  .report-tagline { font-size: 9.5px; color: var(--brand-blue); margin-top: 8px; font-weight: 600; }
</style>
</head>
<body>
<div class="spread">
  <svg class="spread-art" viewBox="0 0 900 636" width="900" height="636">
    <defs>
      <linearGradient id="meeting-tone" x1="0" y1="0" x2="1" y2="1">
        <stop offset="0" stop-color="var(--photo-light)"/>
        <stop offset="0.45" stop-color="#8c8580"/>
        <stop offset="1" stop-color="var(--photo-dark)"/>
      </linearGradient>
    </defs>
    <rect class="back-page" x="0" y="0" width="450" height="636" fill="var(--page-back)"/>
    <rect class="front-page" x="450" y="0" width="450" height="636" fill="var(--page-front)"/>
    <polygon class="meeting-photo" role="img" aria-label="Photo of a team meeting around a conference table"
      points="450,90 720,255 450,500 450,590 62,590" fill="url(#meeting-tone)"/>
    <polygon class="band-light" points="450,20 700,185 720,255 450,90 62,590 0,590 0,545" fill="var(--sky-blue)"/>
    <polygon class="band-mid" points="450,55 705,215 720,255 450,90" fill="var(--mid-blue)"/>
    <polygon class="band-dark-left" points="450,70 450,90 62,590 36,590" fill="var(--brand-blue)"/>
    <polygon class="band-dark-right" points="695,190 900,20 900,75 720,255" fill="var(--brand-blue)"/>
    <line class="spine" x1="450" y1="0" x2="450" y2="636" stroke="rgba(0,0,0,0.08)"/>
  </svg>

  <section class="back-cover">
    <div class="brand-name"><span class="brand-mark"></span>Brim Dental</div>
    <ul class="contact-list">
      <li>
        <svg class="contact-icon" viewBox="0 0 16 16"><circle cx="8" cy="8" r="7" fill="none" stroke="#1d1d1f"/><path d="M8 4a2.5 2.5 0 0 0-2.5 2.5C5.5 9 8 12 8 12s2.5-3 2.5-5.5A2.5 2.5 0 0 0 8 4z" fill="#1d1d1f"/></svg>
        <span>4410 Harrow Lane, Suite 210<br>Ridgefield, KS 66402</span>
      </li>
      <li>
        <svg class="contact-icon" viewBox="0 0 16 16"><circle cx="8" cy="8" r="7" fill="none" stroke="#1d1d1f"/><path d="M5.5 4.5l1.5 0 .7 2-1 .8a5 5 0 0 0 2 2l.8-1 2 .7v1.5c-3.5.5-6.5-2.5-6-6z" fill="#1d1d1f"/></svg>
        <span>800 555 0142</span>
      </li>
      <li>
        <svg class="contact-icon" viewBox="0 0 16 16"><circle cx="8" cy="8" r="7" fill="none" stroke="#1d1d1f"/><rect x="4.5" y="5.5" width="7" height="5" fill="none" stroke="#1d1d1f"/><path d="M4.5 5.5 8 8.3l3.5-2.8" fill="none" stroke="#1d1d1f"/></svg>
        <span>info@brimdental.com</span>
      </li>
      <li><svg class="contact-icon" viewBox="0 0 16 16"><circle cx="8" cy="8" r="7" fill="none" stroke="#1d1d1f"/></svg><span>brimdental</span></li>
      <li><svg class="contact-icon" viewBox="0 0 16 16"><circle cx="8" cy="8" r="7" fill="none" stroke="#1d1d1f"/></svg><span>brimdental</span></li>
      <li><svg class="contact-icon" viewBox="0 0 16 16"><circle cx="8" cy="8" r="7" fill="none" stroke="#1d1d1f"/></svg><span>brimdental</span></li>
    </ul>
  </section>

  <section class="front-cover">
    <div class="brand-name"><span class="brand-mark"></span>Brim Dental</div>
    <div class="report-title">
      <p class="report-kicker">ANNUAL</p>
      <h1 class="report-heading">REPORT 2018</h1>
      <p class="report-tagline">Helping Dentists Get Their Practice Together and Have a Better Life.</p>
    </div>
  </section>
</div>
</body>
</html>
```